Thank you for shopping with us business card

We would like a thank you card for our rebranded business. We used to be "Brindle Goods" but are now "Marlow Finds. Old thank you card and new logo will be attached for reference. New thank you card does not have to be same design as old thank you card, but please use new logo.
Shopmart URL is now marlowfinds.shopmart.example
Instagram is @Marlow_Finds
Email is marlowfinds@mailbox.example
Thank you!

Contact Information for Business Card

Shopmart site, email, Instagram

```html
<!DOCTYPE html>
<html lang="en">
<head>
<meta charset="utf-8">
<title>Marlow Finds – Thank You Card</title>
<link rel="stylesheet" href="https://fonts.googleapis.com/css2?family=Montserrat:wght@700&family=Roboto:wght@300;400;700&display=swap">
<style>
  :root {
    --stage: #3b3b3b;
    --ink: #111111;
    --orange-deep: #ee8a2a;
    --orange-mid: #f6a94f;
    --orange-light: #fcd49a;
    --peach: #fbd9c2;
    --paper: #ffffff;
    --icon: #ef8a33;
  }
  * { box-sizing: border-box; margin: 0; padding: 0; }
  html, body { width: 1200px; height: 1200px; overflow: hidden; }
  body { background: var(--stage); position: relative; font-family: "Roboto", sans-serif; color: var(--ink); }

  .card {
    position: absolute;
    left: 168px;
    width: 864px;
    height: 518px;
    overflow: hidden;
    box-shadow: 0 6px 22px rgba(0,0,0,0.45);
  }
  .card-front { top: 55px; }
  .card-back { top: 629px; }

  .wash { position: absolute; inset: 0; }
  .wash-front {
    background:
      radial-gradient(ellipse 60% 55% at 52% 45%, var(--orange-light) 0%, rgba(252,212,154,0) 70%),
      radial-gradient(ellipse 90% 90% at 50% 50%, var(--orange-mid) 0%, var(--orange-deep) 100%);
  }
  .wash-back {
    background:
      radial-gradient(ellipse 55% 45% at 10% 95%, var(--paper) 0%, rgba(255,255,255,0) 75%),
      radial-gradient(ellipse 60% 40% at 45% 100%, var(--paper) 0%, rgba(255,255,255,0) 80%),
      radial-gradient(ellipse 50% 40% at 55% 45%, var(--peach) 0%, rgba(251,217,194,0) 80%),
      linear-gradient(180deg, var(--orange-mid) 0%, #f8c07a 45%, #fde6d2 100%);
  }

  .wordmark {
    position: absolute;
    left: 0; right: 0;
    top: 240px;
    text-align: center;
    font-family: "Montserrat", sans-serif;
    font-weight: 700;
    font-size: 44px;
    letter-spacing: 0.5px;
    color: var(--ink);
  }

  .thanks-title {
    position: absolute;
    left: 0; right: 0;
    top: 56px;
    text-align: center;
    font-weight: 700;
    font-size: 44px;
    letter-spacing: -0.3px;
  }
  .thanks-message {
    position: absolute;
    left: 0; right: 0;
    top: 132px;
    text-align: center;
    font-weight: 300;
    font-size: 25px;
    line-height: 38.5px;
  }

  .contact-list {
    position: absolute;
    left: 61px;
    top: 354px;
    list-style: none;
  }
  .contact-item {
    display: flex;
    align-items: center;
    height: 38.5px;
    font-size: 20px;
    font-weight: 400;
  }
  .contact-icon {
    width: 26px; height: 26px;
    border-radius: 50%;
    background: var(--icon);
    margin-right: 11px;
    flex: none;
    display: flex; align-items: center; justify-content: center;
  }

  .corner-mark {
    position: absolute;
    right: 56px;
    top: 388px;
    font-family: "Montserrat", sans-serif;
    font-weight: 700;
    font-size: 20px;
    color: var(--ink);
  }
</style>
</head>
<body>

<section class="card card-front">
  <div class="wash wash-front" role="img" aria-label="Orange watercolour wash background"></div>
  <div class="wordmark">MARLOW FINDS</div>
</section>

<section class="card card-back">
  <div class="wash wash-back" role="img" aria-label="Orange and peach watercolour wash fading to white"></div>
  <h1 class="thanks-title">Thank You For Your Purchase</h1>
  <p class="thanks-message">Your purchase made my day and I hope<br>this package brightens yours.<br>Please come back and leave a review!</p>

  <ul class="contact-list">
    <li class="contact-item"><span class="contact-icon"></span>marlowfinds.shopmart.example</li>
    <li class="contact-item">
      <span class="contact-icon">
        <svg width="16" height="12" viewBox="0 0 16 12" aria-hidden="true">
          <rect x="1" y="1" width="14" height="10" fill="none" stroke="#fff" stroke-width="1.4"/>
          <path d="M1 1 L8 7 L15 1 M1 11 L6 6 M15 11 L10 6" fill="none" stroke="#fff" stroke-width="1.2"/>
        </svg>
      </span>marlowfinds@mailbox.example
    </li>
    <li class="contact-item"><span class="contact-icon"></span>@Marlow_Finds</li>
  </ul>

  <div class="corner-mark">Marlow Finds</div>
</section>

</body>
</html>
```